Bath Salt - Sachet Packet (5 Scents) Packaging Design

We sell products to professional salons in the USA. This product is used as the first step when treating clients to a pedicure spa. This product is called SALT SOAK (or Bath Salts). The salt is added to the water to cleanse the skin, create a pleasant fragrance, and change the color of the water.

This product has 5 different variations, based on the scent of the salt soak. The available scents are:
LAVENDER, MANDARIN, CUCUMBER-MELON, JASMINE, MINT.

We would like to see package designs for all 5 scents. The theme should be consistent across the different variations of scents. The design should focus on bright, attractive, floral colors/themes. The design should fully express the color and imagery that are associated with each scent. (Lavender scent should include purple colors, lavender flower, etc.). See example images for reference of popular designs/brands.

Ideal designs will incorporate a luxurious and premium aesthetic that combines elegant imagery, colors, and premium finishes. See example images for reference of popular designs/brands.

Each packet is individually sealed. See dimension artwork file for reference of the sachet packet size and layout.

See the attached document guidelines for more information about product name, key text, and brand logo.

Target Market(s)

Beauty & Nail Salons

Industry/Entity Type

Beauty

Font styles to use
Sans Serif
Script

Requirements
Must have
• Bright imagery and colors that relate to the target fragrance
Nice to have
• Premium and luxurious finishes (shiny accent, etc.)

```html
<!DOCTYPE html>
<html lang="en">
<head>
<meta charset="utf-8">
<title>LUMA Salt Soak – Mandarin</title>
<link href="https://fonts.googleapis.com/css2?family=Josefin+Sans:wght@400;600&family=Playfair+Display:wght@900&family=Great+Vibes&display=swap" rel="stylesheet">
<style>
  :root {
    --bg: #ffffff;
    --orange: #ee7a22;
    --orange-deep: #e46b1a;
    --pouch-white: #fbfbfb;
    --cream: #fbf3d2;
    --gold-light: #fff2a8;
    --gold: #e6c35a;
    --gold-deep: #b8892a;
    --ink: #1a1a1a;
    --text-orange: #e8782a;
  }
  * { margin: 0; padding: 0; box-sizing: border-box; }
  html, body { width: 1110px; height: 1200px; overflow: hidden; background: var(--bg); }
  .canvas { position: relative; width: 1110px; height: 1200px; }

  .pouch {
    position: absolute; left: 233px; top: 172px; width: 642px; height: 872px;
    background: var(--pouch-white); border-radius: 10px; overflow: hidden;
  }
  .pouch-top {
    position: absolute; left: 0; top: 0; width: 100%; height: 442px;
    background: linear-gradient(180deg, var(--orange) 0%, var(--orange-deep) 100%);
  }
  .seal-line {
    position: absolute; left: 0; width: 100%; height: 2px; background: rgba(0,0,0,0.06);
  }
  .seal-line--upper { top: 66px; }
  .seal-line--lower { top: 94px; }

  .brand {
    position: absolute; left: 0; top: 124px; width: 100%; text-align: center;
    font-family: "Josefin Sans", sans-serif; font-weight: 600; font-size: 62px;
    line-height: 1; letter-spacing: 4px; color: var(--ink);
  }
  .title {
    position: absolute; left: 0; top: 214px; width: 100%; text-align: center;
    font-family: "Playfair Display", serif; font-weight: 900; font-size: 74px;
    line-height: 1.1; letter-spacing: 1px;
    background: linear-gradient(180deg, var(--gold-light) 0%, var(--gold) 45%, var(--gold-deep) 100%);
    -webkit-background-clip: text; background-clip: text; color: transparent;
  }

  .label {
    position: absolute; left: 106px; top: 328px; width: 429px; height: 446px;
    background: var(--cream); border: 2px solid var(--orange);
  }
  .label-frame {
    position: absolute; left: 8px; top: 8px; right: 8px; bottom: 8px;
    border: 3px solid var(--orange);
  }
  .fruit-art {
    position: absolute; left: 70px; top: 22px; width: 275px; height: 166px;
    background: radial-gradient(ellipse at 60% 55%, #ffb347 0%, #f7931e 55%, rgba(251,243,210,0) 78%);
    border-radius: 40%;
  }
  .claims {
    position: absolute; left: 38px; top: 202px; width: 300px;
    list-style: none; font-family: "Josefin Sans", sans-serif; font-size: 12.5px;
    letter-spacing: 0.6px; color: var(--text-orange);
  }
  .claims li {
    height: 32px; line-height: 32px; border-bottom: 1px solid var(--orange); white-space: nowrap;
  }
  .claims li:last-child { border-bottom: none; }
  .claims span + span { margin-left: 8px; }

  .scent-bar {
    position: absolute; left: 30px; top: 340px; width: 258px; height: 60px;
    background: var(--orange);
    display: flex; align-items: center; justify-content: center;
  }
  .scent-name {
    font-family: "Great Vibes", cursive; font-size: 40px; line-height: 1;
    background: linear-gradient(180deg, var(--gold-light) 0%, var(--gold) 50%, var(--gold-deep) 100%);
    -webkit-background-clip: text; background-clip: text; color: transparent;
  }
  .badge { position: absolute; left: 304px; top: 328px; }

  .net-weight {
    position: absolute; left: 0; top: 800px; width: 100%; text-align: center;
    font-family: "Josefin Sans", sans-serif; font-size: 13px; letter-spacing: 1px;
    color: var(--text-orange);
  }
</style>
</head>
<body>
<div class="canvas">
  <div class="pouch">
    <div class="pouch-top"></div>
    <div class="seal-line seal-line--upper"></div>
    <div class="seal-line seal-line--lower"></div>

    <div class="brand">LUMA</div>
    <div class="title">SALT SOAK</div>

    <div class="label">
      <div class="label-frame"></div>
      <div class="fruit-art" role="img" aria-label="Illustration of a whole mandarin with a leaf beside a halved mandarin"></div>

      <ul class="claims">
        <li><span>∗ DELUXE PEDICURE</span><span>∗ SINGLE-USE</span></li>
        <li><span>∗ MADE WITH CERTIFIED ORGANIC INGREDIENTS</span></li>
        <li><span>∗ SEALED FRESH</span><span>∗ PARABEN FREE</span></li>
        <li><span>∗ NO TRICLOSAN , SULFATES , 1-2 DIOXANE</span></li>
      </ul>

      <div class="scent-bar"><span class="scent-name">Mandarin</span></div>

      <svg class="badge" width="84" height="84" viewBox="0 0 84 84" aria-hidden="true">
        <circle cx="42" cy="42" r="39" fill="none" stroke="var(--orange)" stroke-width="1.5"/>
        <circle cx="42" cy="42" r="28" fill="none" stroke="var(--orange)" stroke-width="1.2"/>
      </svg>
    </div>

    <div class="net-weight">100g NT WGT</div>
  </div>
</div>
</body>
</html>
```